General contractor/GM consaltant business card

I need a card for my contracting company in North Dakota, we build industrial buildings for the oil feild and oil feild related companies offices, shops, airplain hangars, airports ext. We have a familly atmosphere on the job and are very relational and personal.
Industry/Entity Type
Industrial
Contact Information for Business Card
Kestrelmoor Builders LLC.
Dwight T.Halvorsun
4736 Quillfern dr. Colorado Springs, CO. 80927
Cell# 406-555-8142
dwight@kestrelmoorbuilders.com

```html
<!DOCTYPE html>
<html lang="en">
<head>
<meta charset="utf-8">
<title>Kestrelmoor Builders LLC – Business Card</title>
<link rel="stylesheet" href="https://fonts.googleapis.com/css2?family=Cinzel:wght@400&family=Cabin+Condensed:wght@600&family=Arimo:wght@400&display=swap">
<style>
  :root {
    --page-bg: #d9d4cc;
    --card-bg: #050505;
    --brand-red: #d8323a;
    --brand-blue: #3a6fc4;
    --icon-dark: #050505;
  }
  * { box-sizing: border-box; margin: 0; padding: 0; }
  html, body {
    width: 1200px;
    height: 885px;
    overflow: hidden;
    background: var(--page-bg);
  }
  .canvas {
    position: relative;
    width: 1200px;
    height: 885px;
  }
  .card {
    position: absolute;
    left: 280px;
    width: 640px;
    height: 366px;
    background: var(--card-bg);
    border-radius: 26px;
    box-shadow: 0 10px 28px rgba(0,0,0,0.35);
    overflow: hidden;
  }
  .card--contact { top: 52px; }
  .card--brand { top: 467px; }

  .wordmark {
    position: absolute;
    font-family: "Cabin Condensed", sans-serif;
    font-weight: 600;
    color: var(--brand-red);
    white-space: nowrap;
  }
  .card--contact .wordmark {
    left: 250px;
    top: 250px;
    font-size: 34px;
  }
  .card--brand .wordmark {
    left: 0;
    right: 0;
    top: 130px;
    text-align: center;
    font-size: 52px;
  }

  .holder-name {
    position: absolute;
    font-family: "Cinzel", serif;
    font-weight: 400;
    font-size: 20px;
    letter-spacing: 1px;
    white-space: nowrap;
  }
  .card--contact .holder-name {
    left: 40px;
    top: 300px;
    color: var(--brand-red);
  }
  .card--brand .holder-name {
    left: 0;
    right: 0;
    top: 214px;
    text-align: center;
    color: var(--brand-blue);
    font-size: 22px;
  }

  .contact-list {
    position: absolute;
    right: 70px;
    top: 34px;
    list-style: none;
    text-align: right;
    font-family: "Arimo", sans-serif;
    font-size: 14px;
    line-height: 22px;
    color: var(--brand-blue);
  }
  .contact-icons {
    position: absolute;
    right: 30px;
    top: 36px;
    display: flex;
    flex-direction: column;
    gap: 6px;
  }
  .contact-icon {
    width: 20px;
    height: 20px;
    background: var(--brand-red);
    border-radius: 3px;
    display: block;
  }
</style>
</head>
<body>
<main class="canvas">

  <section class="card card--contact" aria-label="Business card, contact side">
    <ul class="contact-list">
      <li>406-555-8142</li>
      <li>dwight@kestrelmoorbuilders.com</li>
      <li>4736 Quillfern dr.</li>
      <li>Colorado Springs, CO. 80927</li>
    </ul>
    <div class="contact-icons" aria-hidden="true">
      <svg class="contact-icon" viewBox="0 0 20 20">
        <rect width="20" height="20" rx="3" fill="var(--brand-red)"/>
        <rect x="7" y="4" width="6" height="12" rx="1" fill="var(--icon-dark)"/>
      </svg>
      <svg class="contact-icon" viewBox="0 0 20 20">
        <rect width="20" height="20" rx="3" fill="var(--brand-red)"/>
        <rect x="4" y="6" width="12" height="8" fill="var(--icon-dark)"/>
        <path d="M4 6 L10 11 L16 6" fill="none" stroke="var(--brand-red)" stroke-width="1.2"/>
      </svg>
      <svg class="contact-icon" viewBox="0 0 20 20">
        <rect width="20" height="20" rx="3" fill="var(--brand-red)"/>
        <path d="M10 16 C6 11 6 10 6 8.5 A4 4 0 0 1 14 8.5 C14 10 14 11 10 16 Z" fill="var(--icon-dark)"/>
        <circle cx="10" cy="8.5" r="1.5" fill="var(--brand-red)"/>
      </svg>
    </div>
    <p class="wordmark">Kestrelmoor Builders LLC</p>
    <p class="holder-name">Dwight T.Halvorsun</p>
  </section>

  <section class="card card--brand" aria-label="Business card, brand side">
    <p class="wordmark">Kestrelmoor Builders LLC</p>
    <p class="holder-name">Dwight T.Halvorsun</p>
  </section>

</main>
</body>
</html>
```